Beautiful, sharp, website design for family-run property development company.

We are property developers in Kent (south east of London) who want to see the local town change. We are the only local property developer that is a family run business, focussing primarily on converting old, dilapidated Victorian buildings into beautiful residential spaces. Unlike other national developers, we work to regenerate buildings to create new employment opportunities, housing, and revive the town Centre .

Target Market(s)

1. Investors and Joint Venture partners - people with money to invest in property
2. Buyers of property - 25 to 40 year old, young professionals.
3. Commercial funders (people lending money to our projects
4. Professional team: Architects, builders, Estate agent who want to work with us

Industry/Entity Type

Real Estate Development

Coding

Number of Pages Required

Font styles to use
• Please follow the brief of stylish, elegant, modern

Colors

Designer to choose colors to be used in the design.

Requirements
Must have
• Please use these websites as a reference of what we are looking to achieve.
• http://brekmorestudio.com/#page5
• https://palvendro.co.uk/
• http://tamberfold.co.uk/
• http://www.thequarvishgroup.co.uk/about-quarvish
• Clean, simple, elegant, minimal design.
• Images of interiors of houses that have been converted from old buildings
• Images of farm buildings e.g. barns that have been converted to new homes or offices. Images of properties that may have been an old factory or old commercial property that is now a trendy apartment.
• Please use images of properties and interiors that are from the South East of England (including Kent, Surrey, Sussex, Hampshire, Dorset). There is a distinct style of housing in this part of England.
Nice to have
• Colours consistent with our brand colour palette (attached)

```html
<!DOCTYPE html>
<html lang="en">
<head>
<meta charset="utf-8">
<title>Halden Oak Property</title>
<link rel="stylesheet" href="https://fonts.googleapis.com/css2?family=Lato:wght@400;700&display=swap">
<style>
:root{
  --accent:#6f9590;
  --ink:#2b2b2b;
  --body:#3a3a3a;
  --muted:#777;
  --panel:#f1f1f1;
  --card:#f0f0f0;
  --line:#bdbdbd;
  --white:#fff;
}
*{box-sizing:border-box;margin:0;padding:0}
html,body{width:1200px;height:3600px;overflow:hidden;background:var(--white)}
body{position:relative;font-family:'Lato',sans-serif;color:var(--body)}
.abs{position:absolute}
.photo{position:absolute}
h1,h2,h3{font-weight:400;color:var(--ink);letter-spacing:.5px;text-transform:uppercase}
p.copy{font-size:14.5px;line-height:28px;color:var(--body)}
.more{font-size:14px;letter-spacing:1.5px;color:var(--accent);text-transform:uppercase}
.more::after{content:"  \203A\203A";letter-spacing:2px}

/* header */
.brand{left:74px;top:52px;width:170px;text-align:center}
.brand-name{font-size:22px;color:var(--accent);letter-spacing:.5px;display:flex;align-items:center;justify-content:center;gap:8px}
.brand-name i{display:inline-block;width:12px;height:12px;border-radius:50%;background:var(--accent)}
.brand-sub{font-size:9px;letter-spacing:4px;color:var(--muted);margin-top:2px}
.nav{top:67px;font-size:14px;letter-spacing:.5px;color:var(--ink);text-transform:uppercase}
.nav.active{color:var(--accent);font-weight:700}

/* hero */
.hero-card{left:615px;top:214px;width:511px;height:380px;background:var(--card)}
.hero-card h1{position:absolute;left:28px;top:40px;font-size:34px;line-height:36px}
.hero-card p{position:absolute;left:31px;top:128px;width:455px;font-size:14px;line-height:28px}
.hero-card .more{position:absolute;left:31px;top:264px}
.pager{position:absolute;right:26px;top:332px;font-size:14px;display:flex;gap:10px;align-items:center;color:var(--ink)}

/* service cards */
.svc{top:1034px;width:462px;height:300px;background:var(--white);text-align:center}
.svc h2{font-size:32px;line-height:38px;margin-top:38px}
.svc p{font-size:14px;line-height:28px;margin-top:28px;padding:0 20px}
.svc .more{display:inline-block;margin-top:18px}

/* about */
.band{left:0;width:1200px;background:var(--panel)}
.sec-title{font-size:33px}

/* contact */
.field{position:absolute;border-bottom:1px solid var(--line);font-size:12px;color:var(--body);padding-bottom:14px}
.submit{left:974px;top:3416px;width:152px;height:47px;border:2px solid var(--accent);color:var(--accent);font-size:17px;letter-spacing:1px;display:flex;align-items:center;justify-content:center;text-transform:uppercase}
.info{left:74px;font-size:16px;color:var(--ink);display:flex;align-items:center;gap:18px}
.info svg{width:16px;height:16px;fill:var(--ink)}
.social{top:3548px;width:18px;height:18px;border-radius:50%;background:var(--muted)}
</style>
</head>
<body>

<!-- header -->
<div class="abs brand">
  <div class="brand-name"><i></i>HALDEN OAK</div>
  <div class="brand-sub">PROPERTY</div>
</div>
<div class="abs nav active" style="left:511px">Home</div>
<div class="abs nav" style="left:601px">About Us</div>
<div class="abs nav" style="left:718px">Services</div>
<div class="abs nav" style="left:830px">Projects</div>
<div class="abs nav" style="left:947px">Blog</div>
<div class="abs nav" style="left:1030px">Contact Us</div>

<!-- hero -->
<div class="photo" role="img" aria-label="Converted stone barn house with timber-framed windows under a blue sky" style="left:0;top:150px;width:690px;height:508px;background:linear-gradient(180deg,#8fb4dc 0%,#cfdcea 40%,#7d7466 62%,#6c8c3e 100%)"></div>
<div class="abs hero-card">
  <h1>Welcome to<br>Halden Oak Property</h1>
  <p>Mauris sapien augue, efficitur eu diam &nbsp;consequat, interdum sagittis magnadonec eget quam erat. Etiam consectetur hendrerit libero ac interdum tortor at porta lobortis, enim urna venenatis imperdiet tincidunt.</p>
  <div class="more">Read More</div>
  <div class="pager">
    <svg width="14" height="12" viewBox="0 0 14 12"><path d="M6 0 0 6l6 6V8h8V4H6z" fill="#222"/></svg>
    <span>1</span><span>/</span><span>4</span>
    <svg width="14" height="12" viewBox="0 0 14 12"><path d="M8 0l6 6-6 6V8H0V4h8z" fill="#222"/></svg>
  </div>
</div>

<!-- services -->
<div class="photo" role="img" aria-label="Architectural render of a timber-clad house blending into a line sketch" style="left:74px;top:735px;width:513px;height:341px;background:linear-gradient(90deg,#a9c27a 0%,#b98559 35%,#e6e3dc 60%,#f7f7f5 100%)"></div>
<div class="photo" role="img" aria-label="Two developers in hard hats reviewing plans on a construction site with cranes" style="left:615px;top:735px;width:511px;height:341px;background:linear-gradient(180deg,#b9cde0 0%,#d3dbe0 40%,#8b8a80 75%,#a8a59b 100%)"></div>
<div class="abs svc" style="left:100px">
  <h2>Property Redesigned<br>Services</h2>
  <p>Mauris sapien augue, efficitur eu diam<br>consequat, interdum sagittis magnadonec eget quam erat. Etiam consectetur hendrerit libero ac interdum tortor at porta lobortis, enim urna venenatis imperdiet tincidunt.</p>
  <div class="more">Read More</div>
</div>
<div class="abs svc" style="left:640px">
  <h2>Property Developer<br>in Kent</h2>
  <p>Mauris sapien augue, efficitur eu diam<br>consequat, interdum sagittis magnadonec eget quam erat. Etiam consectetur hendrerit libero ac interdum tortor at porta lobortis, enim urna venenatis imperdiet tincidunt.</p>
  <div class="more">Read More</div>
</div>

<!-- about / why us -->
<div class="abs band" style="top:1415px;height:911px"></div>
<h2 class="abs sec-title" style="left:76px;top:1496px">About Us</h2>
<p class="abs copy" style="left:74px;top:1555px;width:340px">Mauris sapien augue, efficitur eu diam consequat, interdum sagittis magnadonec eget quam erat. Etiam consectetur hendrerit libero ac interdum tortor at porta lobortis, enim urna venenatis imperdiet tincidunt.</p>
<div class="abs more" style="left:74px;top:1730px">Read More</div>

<div class="photo" role="img" aria-label="Bright white open-plan interior of a converted barn with exposed roof trusses" style="left:434px;top:1481px;width:422px;height:422px;background:linear-gradient(180deg,#f2f2f2 0%,#dcdcdc 50%,#bdbdbd 100%)"></div>
<div class="photo" role="img" aria-label="Timber roof structure over a large industrial hall with steel railings" style="left:767px;top:1626px;width:359px;height:344px;background:linear-gradient(180deg,#c9883e 0%,#d9a868 45%,#b4b4b0 75%,#9e9e9a 100%)"></div>
<div class="photo" role="img" aria-label="Old brick barn under restoration on a grassy site" style="left:342px;top:1778px;width:362px;height:482px;background:linear-gradient(180deg,#c7d0d8 0%,#b5bcc4 25%,#9a5f45 50%,#6b4a38 70%,#6d8d3a 85%,#5d7d32 100%)"></div>

<h2 class="abs sec-title" style="left:764px;top:2013px">Why Us</h2>
<p class="abs copy" style="left:763px;top:2072px;width:340px">Mauris sapien augue, efficitur eu diam consequat, interdum sagittis magnadonec eget quam erat. Etiam consectetur hendrerit libero ac interdum tortor at porta lobortis, enim urna venenatis imperdiet tincidunt.</p>
<div class="abs more" style="left:763px;top:2247px">Read More</div>

<!-- recent projects -->
<h2 class="abs sec-title" style="left:74px;top:2400px">Recent Projects</h2>
<div class="abs" style="left:1062px;top:2412px;display:flex;gap:14px;align-items:center;font-size:14px;color:var(--ink)">
  <svg width="14" height="12" viewBox="0 0 14 12"><path d="M6 0 0 6l6 6V8h8V4H6z" fill="#222"/></svg>
  <span>/</span>
  <svg width="14" height="12" viewBox="0 0 14 12"><path d="M8 0l6 6-6 6V8H0V4h8z" fill="#222"/></svg>
</div>
<div class="photo" role="img" aria-label="Loft office with dark timber beams, desks and yellow chairs" style="left:74px;top:2476px;width:513px;height:262px;background:linear-gradient(180deg,#5b4b3c 0%,#8a7a66 40%,#cfc7b8 65%,#9a8f80 100%)"></div>
<div class="photo" role="img" aria-label="White converted living space with sofa and long dining table" style="left:615px;top:2476px;width:511px;height:262px;background:linear-gradient(180deg,#f4f4f4 0%,#e2e2e2 55%,#c9c2b6 100%)"></div>
<div class="photo" role="img" aria-label="Red brick apartment blocks against a deep blue sky" style="left:74px;top:2767px;width:513px;height:262px;background:linear-gradient(180deg,#1f6fb8 0%,#4a8bc8 30%,#a4563c 60%,#8a4a34 100%)"></div>
<div class="photo" role="img" aria-label="Stripped-back Victorian room with exposed floor joists and tall windows" style="left:615px;top:2767px;width:511px;height:262px;background:linear-gradient(180deg,#6a5a4e 0%,#a88566 45%,#8a6246 75%,#5c3d2b 100%)"></div>

<!-- contact -->
<div class="abs band" style="top:3094px;height:506px"></div>
<h2 class="abs sec-title" style="left:74px;top:3148px">Contact Us</h2>
<div class="abs" style="left:74px;top:3250px;width:115px;text-align:center">
  <div style="font-size:15px;color:var(--accent);display:flex;align-items:center;justify-content:center;gap:6px"><i style="display:inline-block;width:8px;height:8px;border-radius:50%;background:var(--accent)"></i>HALDEN OAK</div>
  <div style="font-size:6px;letter-spacing:3px;color:var(--muted)">PROPERTY</div>
</div>
<div class="abs" style="left:75px;top:3313px;font-size:16px;line-height:28px;color:var(--ink)">42 Feltmore Lane<br>Ashbridge, KT9 4QX</div>
<div class="abs info" style="top:3380px"><svg viewBox="0 0 16 16"><path d="M3 1l3 3-2 2c1 2 3 4 5 5l2-2 3 3-2 3C7 15 1 9 0 3z"/></svg>1-800-555-0142</div>
<div class="abs info" style="top:3416px"><svg viewBox="0 0 16 16"><path d="M0 3h16v2L8 9 0 5zm0 4 8 4 8-4v6H0z"/></svg>hello@haldenoak.com</div>
<div class="abs info" style="top:3452px"><svg viewBox="0 0 16 16"><path d="M8 0a5 5 0 0 1 5 5c0 4-5 11-5 11S3 9 3 5a5 5 0 0 1 5-5zm0 3a2 2 0 1 0 0 4 2 2 0 0 0 0-4z"/></svg>Map Direction</div>

<div class="field" style="left:615px;top:3200px;width:241px">Name</div>
<div class="field" style="left:886px;top:3200px;width:240px">Email Address</div>
<div class="field" style="left:615px;top:3255px;width:241px">Phone</div>
<div class="field" style="left:886px;top:3255px;width:240px">Subject</div>
<div class="field" style="left:615px;top:3310px;width:511px;height:83px">Message</div>
<div class="abs submit">Submit</div>

<div class="abs" style="left:74px;top:3516px;width:1052px;border-top:1px solid var(--line)"></div>
<div class="abs" style="left:74px;top:3554px;font-size:12px;color:var(--body)">Copyright © 2020 Company Name &nbsp;All Right Reserved</div>
<div class="abs social" style="left:942px"></div>
<div class="abs social" style="left:982px"></div>
<div class="abs social" style="left:1022px"></div>
<div class="abs social" style="left:1062px"></div>
<div class="abs social" style="left:1102px"></div>

</body>
</html>
```